Book cover for a very impressive real-life healing story from a stage IV deadly disease

I need a book cover design for the French translation of the US book http://www.pagevendo.com/Tims-Journey-Fever-Outlasted-Illness/dp/0845512097/ref=sr_1_4?s=books&ie=UTF8&qid=1455100794&sr=1-4&keywords=kit+marsh
.
I do not want the word AIDS on the French cover, as the story of this book applies to any disease.

The french title will be something like :
Un nouveau matin !
Condamné par la médecine, il guérit grâce au jeûne, la détoxination, et l’amour.

which means something like
A new morning!
Subtitle : Given up by official medecine, he managed to heal with fasting, detox and love.

Many thanks !

Target Market(s)

Anybody interested in natural health

Requirements
Must have
• Nothing special
Nice to have
• Nothing special
Should not have
• Nothing special

```html
<!DOCTYPE html>
<html lang="fr">
<head>
<meta charset="utf-8">
<title>Un nouveau matin — couverture</title>
<link href="https://fonts.googleapis.com/css2?family=Bebas+Neue&display=swap" rel="stylesheet">
<style>
  :root {
    --page-bg: #ffffff;
    --red-core: #e12b3f;
    --red-mid: #c41f30;
    --red-edge: #8c1420;
    --band-white: #ffffff;
    --subtitle-red: #c8192c;
    --text-white: #ffffff;
  }
  * { margin: 0; padding: 0; box-sizing: border-box; }
  html, body {
    width: 1200px;
    height: 720px;
    overflow: hidden;
    background: var(--page-bg);
  }
  .canvas {
    position: relative;
    width: 1200px;
    height: 720px;
  }
  .cover {
    position: absolute;
    left: 411px;
    top: 51px;
    width: 378px;
    height: 618px;
    display: flex;
    flex-direction: column;
    font-family: "Bebas Neue", "Arial Narrow", sans-serif;
  }
  .cover-top {
    height: 374px;
    background: radial-gradient(ellipse 75% 70% at 50% 78%, var(--red-core) 0%, var(--red-mid) 45%, var(--red-edge) 100%);
    display: flex;
    align-items: center;
    justify-content: center;
  }
  .title {
    color: var(--text-white);
    font-weight: 400;
    font-size: 100px;
    line-height: 0.9;
    text-align: center;
    letter-spacing: 0.005em;
    padding-top: 10px;
  }
  .title span { display: block; }
  .subtitle-band {
    height: 100px;
    background: var(--band-white);
    display: flex;
    align-items: center;
    justify-content: center;
  }
  .subtitle {
    color: var(--subtitle-red);
    font-size: 20px;
    line-height: 1.2;
    text-align: center;
    font-weight: 400;
  }
  .cover-bottom {
    flex: 1;
    background: radial-gradient(ellipse 80% 120% at 50% 50%, var(--red-mid) 0%, var(--red-edge) 100%);
    display: flex;
    align-items: center;
    justify-content: center;
  }
  .author {
    color: var(--text-white);
    font-size: 24px;
    letter-spacing: 0.32em;
    padding-left: 0.32em;
  }
</style>
</head>
<body>
  <main class="canvas">
    <article class="cover">
      <section class="cover-top">
        <h1 class="title"><span>Un</span><span>Nouveau</span><span>Matin</span></h1>
      </section>
      <section class="subtitle-band">
        <p class="subtitle">Condamné par la médecine, il guérit grâce<br>au jeûne, la détoxination, et l’amour.</p>
      </section>
      <section class="cover-bottom">
        <p class="author">Author Name</p>
      </section>
    </article>
  </main>
</body>
</html>
```